Hello my name is Colin, I am Starting a business called Harbor Health and fitness and am in need of a memorable business card.
It is a personal training studio. I have added the logo that i would like to be on the left center om my business card. i would like room left up the top for a heading sentence such as. "Is your body shocking for all the wrong reasons". there must be room left on the right of the logo below the main heading for 3 sub headings.
then under those 3 headings and logo room for another larger heading eg. "give me a call and learn how to eat chocolate, drink bear and have great sex". in what room is left i would like to be used for my contact details, use I'm Colin Fairweather your fitness expert on the left then on the right Phone, Email and website space in at least 12 Point. Very specific i know :) now onto the back, for the back i would like an eye catching graphic and room for one main headline and 3 bullet points centered just write anything i will choose what to put in them when i pick a winner. Thank you very much for sticking through all of that :) i appreciate you taking the time to read it and hopefully undergo designing me a business card.
I can't wait to see the designs!

Target Market(s)

slightly more towards females although it would probably be best if it was targeted towards both sexes

Industry/Entity Type

Training

Requirements
Nice to have
• I would love to see if anyone could come up with a design that would really make my card stand out and be memorable.
Should not have
• tacky fitness photos of abs and muscles etc.

```html
<!DOCTYPE html>
<html lang="en">
<head>
<meta charset="utf-8">
<title>Harbor Health and Fitness – Business Card</title>
<link rel="stylesheet" href="https://fonts.googleapis.com/css2?family=Questrial&display=swap">
<style>
  :root {
    --navy: #1b4a8c;
    --navy-deep: #163f7a;
    --sky: #c9d6e8;
    --mist: #dfe7f1;
    --ink: #1f4e91;
    --soft-ink: #5f7fae;
    --white: #ffffff;
    --leaf: #a9c98a;
    --leaf-light: #e6efd9;
    --skin: #e2c2a8;
    --page: #ffffff;
  }
  * { box-sizing: border-box; margin: 0; padding: 0; }
  html, body { width: 1200px; height: 848px; overflow: hidden; background: var(--page); }
  body { position: relative; font-family: "Questrial", sans-serif; }

  .card {
    position: absolute;
    top: 278px;
    width: 396px;
    height: 221px;
    overflow: hidden;
    box-shadow: 3px 4px 8px rgba(0,0,0,0.25);
  }
  .card--front {
    left: 165px;
    background: linear-gradient(to bottom, var(--navy-deep) 0%, var(--navy) 25%, #5f84b8 62%, var(--sky) 88%);
  }
  .card--back { left: 609px; }

  .front__headline {
    position: absolute;
    right: 14px;
    top: 6px;
    color: var(--white);
    font-size: 23px;
    line-height: 29px;
    text-align: right;
  }
  .front__brand {
    position: absolute;
    left: 0;
    top: 61px;
    width: 188px;
    height: 74px;
    background: var(--white);
    border-radius: 0 10px 10px 0;
    display: flex;
    align-items: center;
    padding-left: 14px;
    gap: 9px;
  }
  .front__brand-mark {
    width: 16px; height: 16px; border-radius: 50%;
    background: var(--ink); flex: none;
  }
  .front__brand-name {
    color: var(--ink);
    font-size: 19px;
    line-height: 22px;
  }
  .front__subheads {
    position: absolute;
    left: 220px;
    top: 78px;
    list-style: none;
    color: #8fa8cc;
    font-size: 11px;
    line-height: 19px;
  }
  .front__subheads li::before { content: "•"; margin-right: 8px; }
  .front__pitch {
    position: absolute;
    left: 14px;
    right: 12px;
    top: 149px;
    color: #4e6f9f;
    font-size: 11px;
    line-height: 15px;
  }
  .front__pitch strong { color: var(--ink); font-weight: 400; }
  .front__contact {
    position: absolute;
    left: 0; right: 0; bottom: 0;
    height: 28px;
    background: var(--white);
    color: var(--ink);
    font-size: 11.5px;
    display: flex;
    align-items: center;
    padding-left: 14px;
  }

  .back__photo {
    position: absolute; inset: 0;
    background:
      radial-gradient(ellipse 40% 60% at 68% 45%, var(--skin) 0%, rgba(226,194,168,0.6) 45%, rgba(226,194,168,0) 75%),
      linear-gradient(120deg, var(--leaf-light) 0%, var(--leaf) 45%, #c8dcae 70%, var(--leaf-light) 100%);
  }
  .back__headline {
    position: absolute;
    left: 14px;
    top: 11px;
    color: var(--ink);
    font-size: 23px;
    line-height: 28px;
    font-weight: 400;
  }
  .back__points {
    position: absolute;
    left: 14px;
    top: 117px;
    list-style: none;
    color: var(--ink);
    font-size: 11px;
    line-height: 18px;
  }
  .back__points li::before { content: "•"; margin-right: 8px; }
</style>
</head>
<body>
  <section class="card card--front">
    <h1 class="front__headline">Is your body shocking for all the<br>wrong reasons?</h1>
    <div class="front__brand">
      <span class="front__brand-mark"></span>
      <span class="front__brand-name">Harbor Health<br>and Fitness</span>
    </div>
    <ul class="front__subheads">
      <li>Sub Heading 1</li>
      <li>Sub Heading 2</li>
      <li>Sub Heading 3</li>
    </ul>
    <p class="front__pitch">Give me a call and learn how to eat chocolate, drink beer and have great sex! &nbsp;I'm <strong>Colin Fairweather</strong> your fitness expert.</p>
    <p class="front__contact">Tel: 123 555 018 | Email: colin@harborhealth.co.au | Website: www.harborhealth.com</p>
  </section>

  <section class="card card--back">
    <div class="back__photo" role="img" aria-label="Photo of a woman in a headband jogging outdoors against a soft green background"></div>
    <h2 class="back__headline">Is your body<br>shocking for all the<br>wrong reasons?</h2>
    <ul class="back__points">
      <li>Sub Heading 1</li>
      <li>Sub Heading 2</li>
      <li>Sub Heading 3</li>
    </ul>
  </section>
</body>
</html>
```